Education / Investment Website Design (PDF Wireframe Provided)

More details are in the wireframe document

We need a website design for an investment education company. Our Clients purchase education courses through us. We use meridian framework (Wordpress) for our website. We just require the graphics in PSD (not coded) for the

1. Homepage - brightfunnelhub.com style
2. Blog page - brightfunnelhub.com style
3. Single Blog Post
4. Product page - Lernova.com style
5. Single Product Page - https://www.lernova.com/futures-skills-class-australia/?dtcode=kPQwZtn8VB3L
6. Contact Us Page (Contact Us Form, Map and Contact details)
7. About Us Page

See the attached Wireframe for the homepage

IMPORTANT
Websites we like are clean, white, similar to BrightFunnelHub.com and Lernova.com
Use of white space, big fonts, flat buttons

Attached wireframe is the flow of the homepage. (Homepage brief PDF)

Each section represents a "fold" as visitors are scrolling down. (Homepage showing folds PDF - how the visitor sees each section of the homepage as they scroll down the homepage)

We've got a clear idea of the elements on the page and looking for a great graphic / web designer to create those for us. (We do the coding)

Website currently is: southerncapitallearning.com.au (we want to simplify the website and have a more modern / flat design)

Questions: Please ask

Target Market(s)

Investors, People looking for Investment / Financial Education

Industry/Entity Type

Investment

Number of Pages Required

5+ page

Font styles to use
Sans Serif

Requirements
Must have
• Similar Items listed in the wireframe
• Clean Look - Flat design - elegant
• Roll-over (mouse on / mouse off) for Buttons and Top Banner Selection
Should not have
• Images that looks too much like "Stock Images"
• Please avoid bright orange

```html
<!DOCTYPE html>
<html lang="en">
<head>
<meta charset="utf-8">
<title>Blog – Southern Capital Learning</title>
<link href="https://fonts.googleapis.com/css2?family=Lato:wght@300;400;700&family=Montserrat:wght@400;600;700&display=swap" rel="stylesheet">
<style>
:root{
  --teal:#67c8c6;
  --teal-dark:#0e9595;
  --teal-deep:#3fa9a8;
  --grey-bar:#5f5f5f;
  --grey-footer:#666666;
  --ink:#333333;
  --text:#555555;
  --light:#cccccc;
  --white:#ffffff;
}
*{box-sizing:border-box;margin:0;padding:0}
html,body{width:727px;height:1200px;overflow:hidden;background:var(--white)}
body{position:relative;font-family:'Lato',sans-serif;color:var(--text)}
.abs{position:absolute}
.topbar{left:0;top:0;width:727px;height:23px;background:var(--grey-bar)}
.topbar-note{left:97px;top:6px;font:600 7.5px 'Montserrat',sans-serif;color:var(--white);white-space:nowrap}
.search{left:512px;top:0;width:124px;height:23px;background:#8a8a8a;color:#eee;font-size:8.5px;padding:7px 9px}
.search svg{position:absolute;right:9px;top:6px}
.header{left:0;top:23px;width:727px;height:56px;background:var(--teal)}
.brand{left:82px;top:34px;display:flex;align-items:center;gap:6px}
.brand-dot{width:29px;height:29px;border-radius:50%;background:#2d5b78}
.brand-name{font:700 10px 'Montserrat',sans-serif;color:#214d66;letter-spacing:.6px;line-height:1.25;width:130px}
.util{right:91px;top:31px;font:600 7px 'Montserrat',sans-serif;color:var(--white);display:flex;gap:16px}
.nav{right:91px;top:60px;display:flex;gap:16px;font:600 7.5px 'Montserrat',sans-serif;color:var(--white)}
.nav .active{color:#235a66}
.hero{left:0;top:79px;width:727px;height:73px;background:linear-gradient(90deg,#4fb3b3,#78cccb 50%,#5ab9b9)}
.hero h1{position:absolute;width:100%;top:20px;text-align:center;font:400 25px 'Lato',sans-serif;color:var(--white)}
.side-social{left:698px;width:29px;height:24px;background:#d7d7d7}
.crumbs{left:82px;top:162px;font-size:7.5px;color:var(--ink)}
.crumbs b{font-weight:700}
.post{left:82px;width:340px}
.post h2{font:400 25px 'Lato',sans-serif;color:var(--ink);white-space:nowrap}
.meta{margin-top:9px;font-size:7.5px;color:var(--ink);display:flex;gap:18px}
.meta span::before{content:"";display:inline-block;width:6px;height:6px;border:1px solid #555;margin-right:4px;vertical-align:-1px}
.photo{margin-top:24px;width:317px;height:140px;background:linear-gradient(180deg,#c9d9ee 0%,#b7b8a4 35%,#c8b67e 60%,#8b8e8d 80%,#6f7371 100%)}
.excerpt{margin-top:27px;font-size:10px;line-height:16px;color:var(--text)}
.shares{margin-top:20px;display:flex;gap:4px}
.share{width:60px;height:17px;background:var(--light);color:var(--white);font-size:7.5px;display:flex;align-items:center;justify-content:space-between;padding:0 6px 0 10px}
.share.on{background:var(--teal)}
.share i{display:block;width:7px;height:7px;background:var(--white);border-radius:50%}
.read{margin-top:28px;display:inline-block;background:var(--teal-dark);color:var(--white);font:700 8px 'Lato',sans-serif;padding:10px 11px}
.cta{left:465px;width:171px;height:29px;background:var(--teal);display:flex;align-items:center;color:var(--white);font:700 7.5px 'Lato',sans-serif;white-space:nowrap}
.cta-icon{width:31px;height:100%;background:var(--teal-deep);display:flex;align-items:center;justify-content:center}
.cta-icon i{width:11px;height:11px;background:#2f6f70;border-radius:50%}
.cta span{flex:1;text-align:center}
.popular{left:464px;top:360px;width:172px}
.popular h3{font:400 16px 'Lato',sans-serif;color:var(--ink);margin-bottom:24px}
.popular li{list-style:none;font-size:9.5px;line-height:16px;color:var(--text);margin-bottom:8px}
.popular li::before{content:"›";color:var(--teal-dark);font-weight:700;font-size:14px;margin-right:8px}
.footer{left:0;top:1054px;width:727px;height:146px;background:var(--grey-footer);color:#dcdcdc}
.f-brand{left:92px;top:26px;display:flex;align-items:center;gap:5px}
.f-brand .brand-dot{width:18px;height:18px}
.f-brand .brand-name{font-size:7px;width:110px;color:#2d5b78}
.f-legal{left:94px;top:58px;font-size:6.5px;line-height:10.5px;width:120px}
.f-col{top:28px;font-size:6.5px;line-height:10.5px}
.f-col h4{font:700 7.5px 'Lato',sans-serif;color:var(--white);margin-bottom:5px;white-space:nowrap}
</style>
</head>
<body>
<div class="abs topbar"></div>
<div class="abs topbar-note">First time visitor? Then star here and lear more about Southern Capital Learning!</div>
<div class="abs search">Search
<svg width="9" height="9" viewBox="0 0 10 10"><circle cx="4" cy="4" r="3" fill="none" stroke="#fff" stroke-width="1.5"/><line x1="6.2" y1="6.2" x2="9" y2="9" stroke="#fff" stroke-width="1.6"/></svg></div>

<header class="abs header"></header>
<div class="abs brand"><div class="brand-dot"></div><div class="brand-name">SOUTHERN CAPITAL LEARNING</div></div>
<div class="abs util"><span>Sign in | Join</span><span>Contact us</span></div>
<nav class="abs nav"><span>HOME</span><span class="active">BLOG</span><span>PRODUCTS</span><span>ABOUT US</span><span>MEMBERS</span></nav>

<section class="abs hero" role="img" aria-label="Teal-tinted desk photo with notebook and papers"><h1>BLOG</h1></section>

<div class="abs side-social" style="top:110px"></div>
<div class="abs side-social" style="top:141px"></div>
<div class="abs side-social" style="top:171px"></div>
<div class="abs side-social" style="top:202px"></div>

<div class="abs crumbs">Home › <b>Blog</b></div>

<article class="abs post" style="top:206px">
  <h2>Headline aboun the Title</h2>
  <div class="meta"><span>June 10th 2015</span><span>Daniel Mercer</span></div>
  <div class="photo" role="img" aria-label="Sunny coastal street with cars, palm trees and hillside buildings"></div>
  <p class="excerpt">Which investment service do you want to receive today?<br>And be successful.</p>
  <div class="shares"><div class="share"><i></i>1.5k</div><div class="share"><i></i>1.7k</div><div class="share on"><i></i>1.1k</div><div class="share"><i></i>50</div></div>
  <a class="read">READ MORE</a>
</article>

<article class="abs post" style="top:611px">
  <h2>Headline aboun the Title</h2>
  <div class="meta"><span>June 10th 2015</span><span>Daniel Mercer</span></div>
  <div class="photo" role="img" aria-label="Sunny coastal street with cars, palm trees and hillside buildings"></div>
  <p class="excerpt">Which investment service do you want to receive today?<br>And be successful.</p>
  <div class="shares"><div class="share"><i></i>1.5k</div><div class="share"><i></i>1.7k</div><div class="share"><i></i>1.1k</div><div class="share"><i></i>50</div></div>
  <a class="read">READ MORE</a>
</article>

<div class="abs cta" style="top:214px"><div class="cta-icon"><i></i></div><span>TEACH ME HOW TO TRADE</span></div>
<div class="abs cta" style="top:254px;box-shadow:0 2px 3px rgba(0,0,0,.3)"><div class="cta-icon"><i></i></div><span>TELL ME WHAT SHULD I TRADE</span></div>
<div class="abs cta" style="top:293px"><div class="cta-icon"><i></i></div><span>DO ALL THE WORK FOR ME</span></div>

<aside class="abs popular">
  <h3>Popular Posts</h3>
  <ul>
    <li>Buy, then hold and then hope. Not in the current market...</li>
    <li>Farmer's wife trades just like the boys on wall street</li>
  </ul>
</aside>

<footer class="abs footer">
  <div class="abs f-brand"><div class="brand-dot"></div><div class="brand-name">SOUTHERN CAPITAL LEARNING</div></div>
  <div class="abs f-legal">© Copyright 2015 SCL — All right reserved.<br>Terms &amp; Conditions<br>Privacy Policy<br>Contact Us<br>PO BOX Lakeside Central</div>
  <div class="abs f-col" style="left:231px"><h4>MAIN MENU</h4>Home<br>Courses<br>Blog<br>About Us<br>Contact Us</div>
  <div class="abs f-col" style="left:324px"><h4>COURSES</h4>Foundation<br>OME<br>Stock<br>Futures<br>Mindset</div>
  <div class="abs f-col" style="left:418px"><h4>OTHER</h4>FSG<br>Disclaimers<br>Other Legal</div>
  <div class="abs f-col" style="left:511px"><h4>CONNECT US WITH</h4>Facenote<br>Chirper<br>Searchly<br>ViewTube</div>
</footer>
</body>
</html>
```